Sheriff Candidate needs a large yard sign

A candidate for Sheriff needs to have a sign to put in front of businesses and houses that advertise her candidacy.

Target Market(s)

Democrats, voters

Industry/Entity Type

Political

Font styles to use
Sans Serif

Colors
34a7d7
3276b5

Requirements
Must have
• Must have her picture
• Must have the words "Elect Dana Whitlock" - I'd like the name Dana to be smaller Whitlock. "Elect" and "Whitlock" should be the focus.
• at the bottom in a box "Paid for by the Committee to Elect Dana Whitlock"
Nice to have
• it would be good to have her logo as well.
• blue color for democrats and on a white background
Should not have
• pink color

```html
<!DOCTYPE html>
<html lang="en">
<head>
<meta charset="utf-8">
<title>Elect Dana Whitlock – Yard Sign</title>
<link rel="stylesheet" href="https://fonts.googleapis.com/css2?family=Bebas+Neue&family=Oswald:wght@600&family=Mrs+Saint+Delafield&display=swap">
<style>
  :root {
    --democrat-blue: #3276b5;
    --sky-blue: #34a7d7;
    --white: #ffffff;
    --backdrop-light: #8c8a88;
    --backdrop-mid: #6e6c6a;
    --backdrop-dark: #3a3939;
    --hair-brown: #6a4a33;
    --skin-warm: #c99a82;
    --blazer-navy: #1c2233;
    --script-ink: #2b2a2a;
    --seal-gold: #d4a72c;
    --seal-ink: #1f2c45;
  }
  * { margin: 0; padding: 0; box-sizing: border-box; }
  html, body {
    width: 849px;
    height: 1200px;
    overflow: hidden;
    background: var(--white);
  }
  .yard-sign {
    position: relative;
    width: 849px;
    height: 1200px;
    overflow: hidden;
    background: var(--democrat-blue);
  }
  .star-band {
    position: absolute;
    left: 0; top: 0;
    width: 849px;
    height: 60px;
  }
  .portrait {
    position: absolute;
    left: 0; top: 60px;
    width: 849px;
    height: 684px;
    background:
      radial-gradient(ellipse 300px 150px at 420px 640px, var(--blazer-navy) 0%, rgba(28,34,51,0.85) 55%, rgba(28,34,51,0) 100%),
      radial-gradient(ellipse 170px 200px at 345px 300px, var(--skin-warm) 0%, rgba(201,154,130,0.7) 45%, rgba(201,154,130,0) 100%),
      radial-gradient(ellipse 210px 200px at 340px 200px, var(--hair-brown) 0%, rgba(106,74,51,0.5) 50%, rgba(106,74,51,0) 100%),
      radial-gradient(ellipse at 40% 35%, var(--backdrop-light) 0%, var(--backdrop-mid) 50%, var(--backdrop-dark) 100%);
  }
  .slogan-script {
    position: absolute;
    left: 568px;
    top: 285px;
    font-family: "Mrs Saint Delafield", cursive;
    font-size: 74px;
    line-height: 0.95;
    color: var(--script-ink);
    transform: rotate(-30deg);
    transform-origin: left top;
    white-space: nowrap;
  }
  .slogan-script .line-two { display: block; padding-left: 44px; }
  .disclaimer {
    position: absolute;
    left: 34px;
    top: 714px;
    font-family: "Oswald", sans-serif;
    font-weight: 600;
    font-size: 18px;
    letter-spacing: 2px;
    text-transform: uppercase;
    color: var(--white);
    white-space: nowrap;
  }
  .campaign-seal {
    position: absolute;
    left: 542px;
    top: 698px;
    width: 284px;
    height: 284px;
    display: flex;
    align-items: center;
    justify-content: center;
  }
  .seal-disc {
    position: absolute;
    inset: 0;
    border-radius: 50%;
    background: var(--seal-gold);
  }
  .seal-name {
    position: relative;
    font-family: "Bebas Neue", sans-serif;
    font-size: 44px;
    line-height: 1;
    text-align: center;
    color: var(--seal-ink);
  }
  .headline {
    position: absolute;
    left: 0; top: 744px;
    width: 849px;
    height: 456px;
  }
  .headline text {
    font-family: "Bebas Neue", sans-serif;
    fill: var(--white);
  }
</style>
</head>
<body>
<main class="yard-sign">
  <svg class="star-band" viewBox="0 0 849 60" aria-hidden="true">
    <rect width="849" height="60" fill="#3276b5"/>
    <defs>
      <polygon id="band-star" fill="#ffffff"
        points="0,-16 4.7,-5.2 16,-5 7.5,2.6 9.9,13.5 0,7.8 -9.9,13.5 -7.5,2.6 -16,-5 -4.7,-5.2"/>
    </defs>
    <use href="#band-star" x="31" y="30"/>
    <use href="#band-star" x="109" y="30"/>
    <use href="#band-star" x="188" y="30"/>
    <use href="#band-star" x="266" y="30"/>
    <use href="#band-star" x="345" y="30"/>
    <use href="#band-star" x="424" y="30"/>
    <use href="#band-star" x="502" y="30"/>
    <use href="#band-star" x="581" y="30"/>
    <use href="#band-star" x="659" y="30"/>
    <use href="#band-star" x="738" y="30"/>
    <use href="#band-star" x="816" y="30"/>
  </svg>

  <div class="portrait" role="img" aria-label="Candidate photo: head-and-shoulders portrait of Dana Whitlock, smiling, short brown hair, dark navy blazer, grey studio backdrop"></div>

  <p class="slogan-script">Dana for<span class="line-two">Sheriff</span></p>

  <p class="disclaimer">Paid for by the Committee to Elect Dana Whitlock</p>

  <svg class="headline" viewBox="0 0 849 456" aria-label="Elect Whitlock">
    <text x="31" y="226" font-size="270" textLength="490" lengthAdjust="spacingAndGlyphs">ELECT</text>
    <text x="31" y="440" font-size="260" textLength="802" lengthAdjust="spacingAndGlyphs">WHITLOCK</text>
  </svg>

  <div class="campaign-seal">
    <span class="seal-disc"></span>
    <span class="seal-name">Whitlock<br>for Sheriff</span>
  </div>
</main>
</body>
</html>
```